Design of two graphics from basic existing design & colours

I have two graphics which I currently use but they are nothing special. We would like to transform these two graphics, using our existing logo colour, into something special. The outputs will be used:

- on our website;
- in a powerpoint sales presentation;
- in email campaigns; and
- to print for handing to prospects at the end of a sales presentation.

Please just submit one of the graphics and if we like the design, we will ask you to work on the second graphic. These two graphics are critical to our marketing and will be used together so we need them to have a similar look and feel.

```html
<!DOCTYPE html>
<html lang="en">
<head>
<meta charset="utf-8">
<title>Performance Cycle</title>
<link rel="stylesheet" href="https://fonts.googleapis.com/css2?family=Open+Sans:wght@600;700;800&display=swap">
<style>
  :root {
    --bg: #ffffff;
    --ink: #1e1e1e;
    --red: #d9302c;
    --black: #1a1a1a;
    --charcoal: #3b3b3b;
    --grey: #a4a4a4;
    --board: #6b2318;
    --divider: #6b2318;
    --label: #ffffff;
  }
  html, body {
    margin: 0;
    padding: 0;
    width: 1200px;
    height: 999px;
    overflow: hidden;
    background: var(--bg);
  }
  .canvas {
    position: relative;
    width: 1200px;
    height: 999px;
    font-family: "Open Sans", Verdana, sans-serif;
  }
  .cycle-title {
    position: absolute;
    top: 38px;
    left: 0;
    width: 1184px;
    margin: 0;
    text-align: center;
    font-size: 41px;
    line-height: 53px;
    font-weight: 800;
    letter-spacing: 1px;
    color: var(--ink);
  }
  .cycle-wheel {
    position: absolute;
    top: 0;
    left: 0;
  }
  .segment { stroke-width: 12; stroke-linejoin: round; }
  .segment--red { fill: var(--red); stroke: var(--red); }
  .segment--black { fill: var(--black); stroke: var(--black); }
  .segment--charcoal { fill: var(--charcoal); stroke: var(--charcoal); }
  .segment--grey { fill: var(--grey); stroke: var(--grey); }
  .segment-label {
    fill: var(--label);
    font-size: 18px;
    font-weight: 700;
    text-anchor: middle;
  }
  .flow-ring { fill: none; stroke: var(--black); stroke-width: 3.5; }
  .flow-arrow { fill: var(--black); }
  .divider { stroke: var(--divider); stroke-width: 2.5; }
  .board-box { fill: var(--board); }
  .board-label {
    fill: var(--label);
    font-size: 26px;
    font-weight: 700;
    text-anchor: middle;
    letter-spacing: 0.5px;
  }
  .zone-label {
    fill: var(--ink);
    font-size: 19px;
    font-weight: 700;
    text-anchor: middle;
  }
</style>
</head>
<body>
<main class="canvas">
  <h1 class="cycle-title">PERFORMANCE<br>CYCLE</h1>

  <svg class="cycle-wheel" width="1200" height="999" viewBox="0 0 1200 999" aria-label="Performance cycle wheel">
    <defs>
      <path id="segment-shape" d="M499.75 193.7 A349 349 0 0 1 686.25 193.7 L649.38 326.7 A211 211 0 0 0 536.62 326.7 Z"/>
      <polygon id="flow-arrowhead" points="607,350 587,341 587,359"/>
    </defs>

    <line class="divider" x1="177" y1="532" x2="1025" y2="532"/>

    <g class="segments">
      <use href="#segment-shape" class="segment segment--red" transform="rotate(0 593 530)"/>
      <use href="#segment-shape" class="segment segment--black" transform="rotate(36 593 530)"/>
      <use href="#segment-shape" class="segment segment--grey" transform="rotate(72 593 530)"/>
      <use href="#segment-shape" class="segment segment--red" transform="rotate(108 593 530)"/>
      <use href="#segment-shape" class="segment segment--charcoal" transform="rotate(144 593 530)"/>
      <use href="#segment-shape" class="segment segment--red" transform="rotate(180 593 530)"/>
      <use href="#segment-shape" class="segment segment--black" transform="rotate(216 593 530)"/>
      <use href="#segment-shape" class="segment segment--grey" transform="rotate(252 593 530)"/>
      <use href="#segment-shape" class="segment segment--red" transform="rotate(288 593 530)"/>
      <use href="#segment-shape" class="segment segment--charcoal" transform="rotate(324 593 530)"/>
    </g>

    <g class="segment-labels">
      <text class="segment-label" transform="translate(593 246)">
        <tspan x="0" dy="-3">Strategic</tspan><tspan x="0" dy="19">Plan</tspan>
      </text>
      <text class="segment-label" transform="translate(760 296) rotate(52)">
        <tspan x="0" dy="-13">Annual</tspan><tspan x="0" dy="19">Business</tspan><tspan x="0" dy="19">Plan</tspan>
      </text>
      <text class="segment-label" transform="translate(862 443) rotate(72)">
        <tspan x="0" dy="-3">Departmental</tspan><tspan x="0" dy="19">Plan</tspan>
      </text>
      <text class="segment-label" transform="translate(862 618) rotate(-72)">
        <tspan x="0" dy="-22">Annual</tspan><tspan x="0" dy="19">Performance</tspan><tspan x="0" dy="19">Objectives</tspan><tspan x="0" dy="19">&amp; KPI’s</tspan>
      </text>
      <text class="segment-label" transform="translate(764 752) rotate(-38)">
        <tspan x="0" dy="-13">Monthly</tspan><tspan x="0" dy="19">Performance</tspan><tspan x="0" dy="19">Meetings</tspan>
      </text>
      <text class="segment-label" transform="translate(593 812)">
        <tspan x="0" dy="-13">Individual</tspan><tspan x="0" dy="19">Performance</tspan><tspan x="0" dy="19">Plan</tspan>
      </text>
      <text class="segment-label" transform="translate(424 752) rotate(38)">
        <tspan x="0" dy="-13">Individual</tspan><tspan x="0" dy="19">Development</tspan><tspan x="0" dy="19">Plan</tspan>
      </text>
      <text class="segment-label" transform="translate(324 618) rotate(72)">
        <tspan x="0" dy="-3">Succession</tspan><tspan x="0" dy="19">Plan</tspan>
      </text>
      <text class="segment-label" transform="translate(324 443) rotate(-72)">
        <tspan x="0" dy="-3">Business</tspan><tspan x="0" dy="19">Reviews</tspan>
      </text>
      <text class="segment-label" transform="translate(426 296) rotate(-52)">
        <tspan x="0" dy="-13">Advisory</tspan><tspan x="0" dy="19">Board</tspan><tspan x="0" dy="19">Meetings</tspan>
      </text>
    </g>

    <circle class="flow-ring" cx="593" cy="530" r="180"/>
    <g class="flow-arrows">
      <use href="#flow-arrowhead" class="flow-arrow" transform="rotate(4 593 530)"/>
      <use href="#flow-arrowhead" class="flow-arrow" transform="rotate(40 593 530)"/>
      <use href="#flow-arrowhead" class="flow-arrow" transform="rotate(76 593 530)"/>
      <use href="#flow-arrowhead" class="flow-arrow" transform="rotate(109 593 530)"/>
      <use href="#flow-arrowhead" class="flow-arrow" transform="rotate(143 593 530)"/>
      <use href="#flow-arrowhead" class="flow-arrow" transform="rotate(178 593 530)"/>
      <use href="#flow-arrowhead" class="flow-arrow" transform="rotate(215 593 530)"/>
      <use href="#flow-arrowhead" class="flow-arrow" transform="rotate(252 593 530)"/>
      <use href="#flow-arrowhead" class="flow-arrow" transform="rotate(288 593 530)"/>
      <use href="#flow-arrowhead" class="flow-arrow" transform="rotate(324 593 530)"/>
    </g>

    <text class="zone-label" x="600" y="472">Managing Structure</text>
    <rect class="board-box" x="457" y="494" width="286" height="76" rx="8"/>
    <text class="board-label" x="600" y="541">ADVISORY BOARD</text>
    <text class="zone-label" x="600" y="604">Managing Performance</text>
  </svg>
</main>
</body>
</html>
```